Business Cards for a law firm

Business cards for our law firm. Use our silhoette logo and OAK HARBOR - check our website (www.oakharbor-legal.com)

Contact Information for Business Card

our silhouette logo, OAK HARBOR, 800-555-0147, Dorian Kestrup, dorian@oakharbor-legal.com

Requirements
Must have
• our silhouette logo, OAK HARBOR, 800-555-0147, Dorian Kestrup, dorian@oakharbor-legal.com

```html
<!DOCTYPE html>
<html lang="en">
<head>
<meta charset="utf-8">
<title>Oak Harbor Business Cards</title>
<link rel="stylesheet" href="https://fonts.googleapis.com/css2?family=Montserrat:wght@400;500;600;700&display=swap">
<style>
  :root {
    --navy: #22336c;
    --ink: #1f1f24;
    --paper: #ffffff;
    --backdrop: #3b3b3d;
  }
  * { margin: 0; padding: 0; box-sizing: border-box; }
  html, body { width: 1200px; height: 1059px; overflow: hidden; }
  body {
    background: var(--backdrop);
    font-family: "Montserrat", sans-serif;
    position: relative;
  }
  .card {
    position: absolute;
    box-shadow: 6px 10px 18px rgba(0,0,0,0.45);
  }
  .card-front {
    left: 256px; top: 100px; width: 688px; height: 391px;
    background: var(--paper);
  }
  .card-back {
    left: 253px; top: 537px; width: 694px; height: 394px;
    background: var(--navy);
  }
  .brand {
    position: absolute;
    display: flex; align-items: center;
    font-weight: 700; letter-spacing: 0.02em;
    white-space: nowrap;
  }
  .brand-mark { border-radius: 50%; flex: none; }
  .card-front .brand {
    left: 64px; top: 174px;
    color: var(--navy); font-size: 21px; gap: 12px;
  }
  .card-front .brand-mark { width: 30px; height: 30px; background: var(--navy); }
  .card-back .brand {
    left: 0; right: 0; top: 165px; justify-content: center;
    color: var(--paper); font-size: 44px; gap: 22px;
  }
  .card-back .brand-mark { width: 60px; height: 60px; background: var(--paper); }
  .divider {
    position: absolute; left: 343px; top: 87px;
    width: 2px; height: 218px; background: var(--navy);
  }
  .details { position: absolute; left: 380px; top: 84px; color: var(--ink); }
  .person-name {
    color: var(--navy); font-weight: 700; font-size: 23px; letter-spacing: 0.01em;
    line-height: 1.2;
  }
  .person-role { font-size: 15px; font-weight: 500; margin-top: 2px; letter-spacing: 0.02em; }
  .address { font-size: 15.5px; line-height: 20px; margin-top: 30px; }
  .contacts { list-style: none; margin-top: 30px; }
  .contacts li {
    display: flex; align-items: center; gap: 11px;
    font-size: 15.5px; height: 26.5px;
  }
  .contacts svg { width: 13px; height: 13px; flex: none; fill: var(--navy); }
</style>
</head>
<body>
  <section class="card card-front">
    <div class="brand"><span class="brand-mark"></span>OAK HARBOR</div>
    <div class="divider"></div>
    <div class="details">
      <h1 class="person-name">DORIAN KESTRUP</h1>
      <p class="person-role">OWNER</p>
      <p class="address">4120 Harbor View Rd #310,<br>Marin Bay, CA 94017</p>
      <ul class="contacts">
        <li>
          <svg viewBox="0 0 24 24" aria-hidden="true"><path d="M6.6 10.8c1.4 2.8 3.8 5.1 6.6 6.6l2.2-2.2c.3-.3.7-.4 1-.2 1.1.4 2.3.6 3.6.6.6 0 1 .4 1 1V20c0 .6-.4 1-1 1C10.6 21 3 13.4 3 4c0-.6.4-1 1-1h3.5c.6 0 1 .4 1 1 0 1.3.2 2.5.6 3.6.1.3 0 .7-.2 1z"/></svg>
          800-555-0147
        </li>
        <li>
          <svg viewBox="0 0 24 24" aria-hidden="true"><path d="M2 4h20v16H2zm2 2v1l8 5 8-5V6l-8 5z"/></svg>
          dorian@oakharbor-legal.com
        </li>
        <li>
          <svg viewBox="0 0 24 24" aria-hidden="true"><path d="M12 2a10 10 0 100 20 10 10 0 000-20zm0 2c.9 0 2.4 2 2.9 5H9.1C9.6 6 11.1 4 12 4zM4.3 10h3.2a18 18 0 000 4H4.3a8 8 0 010-4zm4.8 5h5.8c-.5 3-2 5-2.9 5s-2.4-2-2.9-5zm7.4-1a18 18 0 000-4h3.2a8 8 0 010 4z"/></svg>
          www.oakharbor-legal.com
        </li>
      </ul>
    </div>
  </section>

  <section class="card card-back">
    <div class="brand"><span class="brand-mark"></span>OAK HARBOR</div>
  </section>
</body>
</html>
```